Need Professional, Modern, Clean Newsletter Templates for High End Real Estate Agents in Orange Coun

I need a newsletter for realtors who specialize in high-end home sales for Orange County, California. Please see the attached draft of the newsletter we have in mind. Please note the logo at the top and the beach imagery and please use these and complementary fonts, colors and themes when creating your design. These particular realtors focus on very high-end clients with a specialization on ocean front properties. I WANT YOU TO PLEASE USE THE HEADER FROM MY ATTACHMENT IN YOUR NEWSLETTER. THIS NEWSLETTER IS INTENDED TO BE SENT OUT VIA EMAIL ONLY, NOT PRINT.

The idea behind the newsletter is that it will cover four broad categories. We will have a content creator who will pull content each week, however we need a nice looking template that can support their content. These are the four categories :

1) Market Data - this will pull graphs and information that the realtors receive, directly from the MLS (home listing site). Most of this will be in graph or table form, so we need a nice way to support that.

2.) Featured Listings - this will show the featured homes they have for sale at any given time. This section of the template should have a place to put pictures of the home with supporting text.

3.) News you can use - links to videos and articles relevant to the real estate industry and in the area.

4.) Upcoming OC Events - list of upcoming events in the area.

I feel like I need to post this update in case there was some confusion in my contest brief.

I DO NOT want a new logo or header design. What I am looking for is a newsletter to support the header and logo I already have, and for a nice template which includes each of the four sections I described in my brief. I would like you to think about each of the four sections and design them accordingly. There needs to be a good section for graphs (market data), for videos, for featured listings (pictures of homes with supporting descriptive text) and upcoming events (maybe supported by a calendar and text sections to describe the event, etc.)

This newsletter will be sent out as email only. Your entries should be made as .pdf or as a word document. Thanks.

Target Market(s)

High end real estate buyers and sellers, with a focus on ocean front property.

Industry/Entity Type

Real Estate

Colors
33a6d7
00a990
86cae6

Requirements
Must have
• You MUST include the header photo from the .png attachment I included. "Kestwin Shoreline Homes - Your Coastal Closers."

```html
<!DOCTYPE html>
<html lang="en">
<head>
<meta charset="utf-8">
<title>Kestwin Shoreline Homes – Newsletter</title>
<link href="https://fonts.googleapis.com/css2?family=Lato:wght@400;700&family=Raleway:wght@300;400&display=swap" rel="stylesheet">
<style>
:root{
  --page:#3b3b3b;
  --white:#ffffff;
  --ocean:#33a6d7;
  --ocean-dark:#1f86b8;
  --sky:#86cae6;
  --teal:#00a990;
  --welcome:#1ea7d3;
  --panel:#eceff0;
  --ink:#333a3f;
  --muted:#7d8589;
  --rule:#cfd4d6;
  --bar-bg:#d5e5ec;
  --bar:#3ab8b0;
  --social:#33a6d7;
  --stay:#e4e6e7;
}
*{box-sizing:border-box;margin:0;padding:0}
html,body{width:1200px;height:3863px;overflow:hidden}
body{background:var(--page);font-family:"Lato",Arial,sans-serif;color:var(--ink)}
.sheet{position:absolute;left:200px;top:0;width:800px;height:3863px;background:var(--white)}
section{position:absolute;left:0;width:800px}
.abs{position:absolute}

/* nav */
.nav{top:0;height:108px;display:flex;justify-content:center;align-items:center;gap:64px}
.nav a{font-size:17px;color:#4a4f52;text-decoration:none;letter-spacing:.3px}

/* hero */
.hero{top:108px;height:325px;background:linear-gradient(180deg,#4f8fc4 0%,#8ec5e4 28%,#1e9fc4 48%,#29b3c8 62%,#d9e9e6 80%,#e8ddc9 100%)}
.brand-card{left:36px;top:88px;width:144px;height:144px;background:var(--white);display:flex;align-items:center;justify-content:center;text-align:center}
.brand-card span{font-family:"Raleway",sans-serif;font-weight:300;font-size:21px;line-height:1.2;color:var(--ocean);letter-spacing:1px;text-transform:uppercase}
.hero-tagline{left:420px;width:380px;top:120px;text-align:center;font-family:"Raleway",sans-serif;font-weight:300;font-size:31px;letter-spacing:3px;color:var(--white)}

/* welcome */
.welcome{top:433px;height:216px;background:var(--welcome);color:var(--white);text-align:center;padding:38px 60px 0}
.welcome h1{font-size:32px;font-weight:700;margin-bottom:22px}
.welcome p{font-size:16.5px;line-height:30px}

/* intro letter */
.letter{top:649px;height:412px}
.portrait-frame{left:16px;top:64px;width:211px;height:278px;background:#d2d4d5;padding:11px}
.portrait{width:100%;height:100%;background:linear-gradient(160deg,#5f5a55 0%,#8a8580 40%,#3d4046 100%)}
.letter-body{left:258px;top:78px;width:510px}
.letter-body h2{font-size:26px;color:var(--teal);font-weight:700;padding-bottom:14px;border-bottom:2px solid var(--rule)}
.letter-body p{font-size:16.5px;line-height:33px;color:var(--muted);padding:10px 0 16px;border-bottom:2px solid var(--rule)}
.letter-body .agent{font-size:21px;font-weight:700;margin-top:18px;color:var(--ink)}
.letter-body .email{font-size:17px;font-weight:700;color:var(--teal);margin-top:6px;display:block;text-decoration:none}

/* feature grid */
.topics{top:1061px;height:536px;background:var(--panel)}
.topic{width:392px;text-align:center}
.topic .icon{width:78px;height:78px;margin:0 auto}
.topic h3{font-size:21px;font-weight:400;color:var(--ink);margin-top:30px}
.topic p{font-size:16px;line-height:28px;color:var(--muted);margin-top:10px}

/* market table */
.market{top:1653px;height:484px;background:var(--panel)}
.market table{border-collapse:collapse;width:800px}
.market th{height:62px;background:var(--teal);color:var(--white);font-size:17px;font-weight:700}
.market th:first-child{text-align:left;padding-left:26px}
.market td{height:42px;font-size:16px;color:#5a6165;text-align:center;border-left:4px solid var(--white)}
.market td:first-child{text-align:left;padding-left:26px;border-left:none;width:203px}
.market tr.spacer td{height:18px}
.market tr.trend td{height:62px;vertical-align:bottom}
.market tr.links td{height:48px;vertical-align:middle}
.market .see{color:var(--teal);font-size:16px}

/* featured listing */
.listing{top:2209px;height:438px;background:var(--panel)}
.band{height:62px;background:var(--teal);color:var(--white);font-size:17px;font-weight:700;padding:22px 26px 0;letter-spacing:.3px}
.listing-info{left:31px;top:105px;font-size:17px;line-height:28px;color:#4a5054}
.price{font-size:30px;color:#1d4e6a;margin:12px 0 16px;display:block}
.view-link{display:block;margin-top:16px;color:#1d4e6a;text-decoration:underline;font-size:17px}
.listing-chart{left:305px;top:62px}

/* news */
.news{top:2737px;height:358px;background:var(--ocean)}
.news h2{text-align:center;color:var(--white);font-size:31px;font-weight:400;padding-top:46px}
.video{top:152px;width:210px;height:137px;background:var(--ocean-dark);padding:8px}
.video .screen{width:100%;height:100%;background:linear-gradient(180deg,#2c3440 0%,#6d7b8c 55%,#1c1f24 100%);display:flex;align-items:center;justify-content:center}

/* events */
.events{top:3095px;height:453px}
.events h2{position:absolute;left:31px;top:42px;font-size:17px;color:var(--ocean);font-weight:700;letter-spacing:.5px}
.date{width:67px;height:82px;border:2px solid var(--ocean);text-align:center}
.date .day{font-size:28px;font-weight:700;color:#2e4654;height:44px;line-height:44px}
.date .month{background:var(--ocean);color:var(--white);font-size:16px;height:34px;line-height:34px}
.story{left:127px;width:640px}
.story h3{font-size:19px;font-weight:700;color:var(--ink)}
.story p{font-size:14px;line-height:26px;color:#5a6165;margin-top:10px}
.story a{display:block;font-size:14px;color:var(--ocean);font-weight:700;margin-top:4px;text-decoration:none}

/* stay in touch */
.stay{top:3548px;height:98px;background:var(--stay)}
.stay span{position:absolute;left:31px;top:33px;font-family:"Raleway",sans-serif;font-size:27px;color:#5e6569;letter-spacing:1.5px}
.social{top:27px;width:44px;height:44px;background:var(--social)}

/* footer */
.footer{top:3646px;height:217px;text-align:center;font-size:14.5px;color:#8a9194}
.footer p{position:absolute;left:0;width:800px}
.footer a{color:var(--ocean);text-decoration:none}
</style>
</head>
<body>
<div class="sheet">

  <nav class="nav" style="position:absolute;left:0;width:800px">
    <a href="#">MARKET DATA</a>
    <a href="#">FEATURED LISTINGS</a>
    <a href="#">REAL ESTATE NEWS</a>
    <a href="#">OC EVENTS</a>
  </nav>

  <section class="hero" role="img" aria-label="Beach photograph: turquoise ocean and surf rolling onto sand under a blue sky">
    <div class="abs brand-card"><span>Kestwin Shoreline Homes</span></div>
    <div class="abs hero-tagline">YOUR COASTAL CLOSERS</div>
  </section>

  <section class="welcome">
    <h1>Welcome To High End Real Estate</h1>
    <p>Elementum pellentesque aliquet. Nullam sodales urna erat, vitae egestas nisl tincidunt et. Sed iaculis rhoncus dolor. Integer vel urna nec elit varius dapibus ac nec mi. Vestibulum at nulla nec nulla pharetra sollicitudin.</p>
  </section>

  <section class="letter">
    <div class="abs portrait-frame"><div class="portrait" role="img" aria-label="Portrait photograph of agent Reid Halvorsen in a grey suit"></div></div>
    <div class="abs letter-body">
      <h2>JAN 2014 NEWSLETTER</h2>
      <p>Elementum pellentesque aliquet. Nullam sodales urna erat, vitae egestas nisl tincidunt et. Sed iaculis rhoncus dolor. Integer vel urna nec elit varius dapibus ac nec mi. Vestibulum at nulla nec nulla pharetra sollicitudin.</p>
      <div class="agent">REID HALVORSEN</div>
      <a class="email" href="#">Email Me</a>
    </div>
  </section>

  <section class="topics">
    <div class="abs topic" style="left:8px;top:41px">
      <svg class="icon" viewBox="0 0 78 78"><circle cx="39" cy="39" r="36" fill="none" stroke="#33a6d7" stroke-width="3"/><path d="M22 40 L39 24 L56 40" fill="none" stroke="#33a6d7" stroke-width="3.5" stroke-linejoin="round"/><path d="M27 37 V54 H51 V37" fill="#33a6d7"/><rect x="35" y="44" width="8" height="10" fill="#fff"/></svg>
      <h3>Real Estate Market Data</h3>
      <p>Track monthly changes in property values<br>and market trends</p>
    </div>
    <div class="abs topic" style="left:400px;top:41px">
      <svg class="icon" viewBox="0 0 78 78"><circle cx="39" cy="39" r="36" fill="none" stroke="#33a6d7" stroke-width="3"/><rect x="28" y="22" width="22" height="34" fill="#33a6d7"/><g fill="#fff"><rect x="32" y="27" width="5" height="5"/><rect x="41" y="27" width="5" height="5"/><rect x="32" y="36" width="5" height="5"/><rect x="41" y="36" width="5" height="5"/><rect x="36" y="46" width="6" height="10"/></g></svg>
      <h3>Featured Property Listings</h3>
      <p>Some of the best properties presently<br>available for sale in OC</p>
    </div>
    <div class="abs topic" style="left:8px;top:278px">
      <svg class="icon" viewBox="0 0 78 78"><circle cx="39" cy="39" r="36" fill="none" stroke="#33a6d7" stroke-width="3"/><path d="M24 34 L46 24 V52 L24 42 Z" fill="#33a6d7"/><rect x="26" y="42" width="7" height="12" fill="#33a6d7"/><path d="M50 32 Q55 38 50 44" fill="none" stroke="#33a6d7" stroke-width="3"/></svg>
      <h3>News You Can Use</h3>
      <p>Follow latest news and issues impacting<br>the real estate market</p>
    </div>
    <div class="abs topic" style="left:400px;top:278px">
      <svg class="icon" viewBox="0 0 78 78"><circle cx="39" cy="39" r="36" fill="none" stroke="#33a6d7" stroke-width="3"/><rect x="25" y="25" width="28" height="28" rx="2" fill="none" stroke="#33a6d7" stroke-width="3"/><rect x="25" y="25" width="28" height="7" fill="#33a6d7"/><g fill="#33a6d7"><rect x="30" y="37" width="4" height="4"/><rect x="37" y="37" width="4" height="4"/><rect x="44" y="37" width="4" height="4"/><rect x="30" y="44" width="4" height="4"/><rect x="37" y="44" width="4" height="4"/></g></svg>
      <h3>OC Community Events</h3>
      <p>Upcoming events note in the Orange<br>County community</p>
    </div>
  </section>

  <section class="market">
    <table>
      <thead><tr><th>Zip Code:</th><th>92677</th><th>92651</th><th>92672</th><th>92673</th><th>92629</th></tr></thead>
      <tbody>
        <tr class="spacer"><td></td><td></td><td></td><td></td><td></td><td></td></tr>
        <tr><td>Monthly Units Sold</td><td>115</td><td>116</td><td>117</td><td>118</td><td>119</td></tr>
        <tr><td>Avg. Sold Price</td><td>$583K</td><td>$583K</td><td>$583K</td><td>$583K</td><td>$583K</td></tr>
        <tr><td>Sold % of Orig List $</td><td>95.5%</td><td>95.5%</td><td>95.5%</td><td>95.5%</td><td>95.5%</td></tr>
        <tr><td>Current Units Listed</td><td>122</td><td>122</td><td>122</td><td>122</td><td>122</td></tr>
        <tr><td>Avg. List Price</td><td>$1,415K</td><td>$1,415K</td><td>$1,415K</td><td>$1,415K</td><td>$1,415K</td></tr>
        <tr><td>Avg. Days on Market</td><td>83</td><td>83</td><td>83</td><td>83</td><td>83</td></tr>
        <tr class="trend">
          <td style="vertical-align:middle">Historical Trends</td>
          <td><svg width="44" height="44" viewBox="0 0 44 44"><circle cx="22" cy="22" r="19" fill="none" stroke="#00a990" stroke-width="3.5"/><g fill="#00a990"><rect x="14" y="22" width="4" height="9"/><rect x="20" y="17" width="4" height="14"/><rect x="26" y="13" width="4" height="18"/></g></svg></td>
          <td><svg width="44" height="44" viewBox="0 0 44 44"><circle cx="22" cy="22" r="19" fill="none" stroke="#00a990" stroke-width="3.5"/><g fill="#00a990"><rect x="14" y="22" width="4" height="9"/><rect x="20" y="17" width="4" height="14"/><rect x="26" y="13" width="4" height="18"/></g></svg></td>
          <td><svg width="44" height="44" viewBox="0 0 44 44"><circle cx="22" cy="22" r="19" fill="none" stroke="#00a990" stroke-width="3.5"/><g fill="#00a990"><rect x="14" y="22" width="4" height="9"/><rect x="20" y="17" width="4" height="14"/><rect x="26" y="13" width="4" height="18"/></g></svg></td>
          <td><svg width="44" height="44" viewBox="0 0 44 44"><circle cx="22" cy="22" r="19" fill="none" stroke="#00a990" stroke-width="3.5"/><g fill="#00a990"><rect x="14" y="22" width="4" height="9"/><rect x="20" y="17" width="4" height="14"/><rect x="26" y="13" width="4" height="18"/></g></svg></td>
          <td><svg width="44" height="44" viewBox="0 0 44 44"><circle cx="22" cy="22" r="19" fill="none" stroke="#00a990" stroke-width="3.5"/><g fill="#00a990"><rect x="14" y="22" width="4" height="9"/><rect x="20" y="17" width="4" height="14"/><rect x="26" y="13" width="4" height="18"/></g></svg></td>
        </tr>
        <tr class="links"><td></td><td class="see">See Chart</td><td class="see">See Chart</td><td class="see">See Chart</td><td class="see">See Chart</td><td class="see">See Chart</td></tr>
      </tbody>
    </table>
  </section>

  <section class="listing">
    <div class="band">FEATURED LISTINGS</div>
    <div class="abs listing-info">
      412 Tidewater Lane<br>Laguna Niguel, CA 92677
      <span class="price">$489,900</span>
      Bedrooms: 2 beds<br>Bathrooms: 2 full<br>Sq. Footage: 1,200<br>MLS# OC10482236
      <a class="view-link" href="#">View Listing Details</a>
    </div>
    <svg class="abs listing-chart" width="475" height="250" viewBox="0 0 475 250" font-family="Lato, sans-serif">
      <g font-size="11" fill="#7d8589" text-anchor="end">
        <text x="18" y="60">500</text><text x="18" y="87">400</text><text x="18" y="114">300</text><text x="18" y="141">200</text><text x="18" y="168">100</text><text x="18" y="195">0</text>
      </g>
      <g fill="#d5e5ec">
        <rect x="28" y="56" width="16" height="135"/><rect x="60" y="56" width="16" height="135"/><rect x="92" y="56" width="16" height="135"/><rect x="124" y="56" width="16" height="135"/><rect x="156" y="56" width="16" height="135"/><rect x="188" y="56" width="16" height="135"/><rect x="220" y="56" width="16" height="135"/><rect x="252" y="56" width="16" height="135"/><rect x="284" y="56" width="16" height="135"/><rect x="316" y="56" width="16" height="135"/><rect x="348" y="56" width="16" height="135"/><rect x="380" y="56" width="16" height="135"/><rect x="412" y="56" width="16" height="135"/><rect x="444" y="56" width="16" height="135"/>
      </g>
      <g fill="#3ab8b0">
        <rect x="28" y="178" width="16" height="13"/><rect x="60" y="126" width="16" height="65"/><rect x="92" y="121" width="16" height="70"/><rect x="124" y="91" width="16" height="100"/><rect x="156" y="142" width="16" height="49"/><rect x="188" y="129" width="16" height="62"/><rect x="220" y="159" width="16" height="32"/><rect x="252" y="180" width="16" height="11"/><rect x="284" y="105" width="16" height="86"/><rect x="316" y="89" width="16" height="102"/><rect x="348" y="121" width="16" height="70"/><rect x="380" y="132" width="16" height="59"/><rect x="412" y="148" width="16" height="43"/><rect x="444" y="169" width="16" height="22"/>
      </g>
      <g font-size="12" fill="#5a6165" text-anchor="middle" font-weight="700">
        <text x="36" y="214">S</text><text x="68" y="214">M</text><text x="100" y="214">T</text><text x="132" y="214">W</text><text x="164" y="214">T</text><text x="196" y="214">F</text><text x="228" y="214">S</text><text x="260" y="214">S</text><text x="292" y="214">M</text><text x="324" y="214">T</text><text x="356" y="214">W</text><text x="388" y="214">T</text><text x="420" y="214">F</text><text x="452" y="214">S</text>
      </g>
      <rect x="40" y="4" width="212" height="48" fill="#2c3a44"/>
      <path d="M124 52 L132 60 L140 52 Z" fill="#2c3a44"/>
      <text x="146" y="33" font-size="12" fill="#ffffff" text-anchor="middle">Wednesday, December 3</text>
    </svg>
  </section>

  <section class="news">
    <h2>News You Can Use</h2>
    <div class="abs video" style="left:52px"><div class="screen" role="img" aria-label="Video still from a real estate news broadcast"><svg width="44" height="44" viewBox="0 0 44 44"><circle cx="22" cy="22" r="20" fill="#ffffff"/><path d="M17 13 L31 22 L17 31 Z" fill="#222"/></svg></div></div>
    <div class="abs video" style="left:292px"><div class="screen" role="img" aria-label="Video still from a housing market news segment"></div></div>
    <div class="abs video" style="left:531px"><div class="screen" role="img" aria-label="Video still from a mortgage rates news segment"></div></div>
  </section>

  <section class="events">
    <h2>FEATURED LISTINGS</h2>
    <div class="abs date" style="left:36px;top:106px"><div class="day">25</div><div class="month">Feb</div></div>
    <div class="abs story" style="top:112px">
      <h3>Full width news story area</h3>
      <p>Lorem ipsum dolor sit amet, consectetur adipiscing elit. Nulla vitae enim metus. Praesent sit amet mauris arcu, eu molestie nis. Lorem ipsum dolor sit amet, consectetur adipiscing elit. Nulla vitae enim metus. Praesent sit amet mauris arcu, eu molestie nis.</p>
      <a href="#">Read more</a>
    </div>
    <div class="abs date" style="left:36px;top:258px"><div class="day">25</div><div class="month">Feb</div></div>
    <div class="abs story" style="top:264px">
      <h3>Commented code allows more stories to be added easily</h3>
      <p>Lorem ipsum dolor sit amet, consectetur adipiscing elit. Nulla vitae enim metus. Praesent sit amet mauris arcu, eu molestie nis. Lorem ipsum dolor sit amet, consectetur adipiscing elit. Nulla vitae enim metus. Praesent sit amet mauris arcu, eu molestie nis.</p>
      <a href="#">Read more</a>
    </div>
  </section>

  <section class="stay">
    <span>Stay In Touch With Us:</span>
    <a class="abs social" style="left:475px" href="#" aria-label="Social channel 1"></a>
    <a class="abs social" style="left:538px" href="#" aria-label="Social channel 2"></a>
    <a class="abs social" style="left:601px" href="#" aria-label="Social channel 3"></a>
    <a class="abs social" style="left:664px" href="#" aria-label="Social channel 4"></a>
    <a class="abs social" style="left:727px" href="#" aria-label="Social channel 5"></a>
  </section>

  <footer class="footer" style="position:absolute;top:3646px;left:0;width:800px;height:217px">
    <p style="top:58px">Copyright © 2014 Kestwin Shoreline Homes, All rights reserved.</p>
    <p style="top:94px">Our mailing address is: Kestwin Shoreline Homes 18 Harbor Crest Lane Dana Point, CA 92629</p>
    <p style="top:125px"><a href="#">unsubscribe from this list</a> | <a href="#">update subscription preferences</a></p>
  </footer>

</div>
</body>
</html>
```